Design for Bright Oak Homes real estate agency

Incorporate logo into new business cards. I need to include the Harlow Pemberton logo incorporated into Bright Oak Homes on one side of the card (attached). On the other side I see just the icon with "Merle Dunaway" (attached) with "Rooted in Care" either included as is or removed from logo and rather put as a tag line on the business card separate from the main logo. Contact information:

Merle Dunaway
Associate Broker
Cell: 555-307-1948
Email: merledunaway@brightoakhomes.example
Web: www.brightoakhomes.example

Target Market(s)

Buyers, Sellers, Builders and Investors of homes and land

Industry/Entity Type

Real Estate Agent

Contact Information for Business Card

My client base tend to be higher end home buyers, sellers, builders and investors. I have been more and more in land and subdivisions for builders and investors. The card should not be cluttered. Clean and simple - yet with an air of exclusive/high end

Colors

Designer to choose colors to be used in the design.

Requirements
Must have
• Must have the logo on one side that has Harlow Pemberton logo incorporated. The side that has my contact information does not have to have the Harlow Pemberton logo incorporated.
• Must include "Rooted in Care" tag line either within logo (as is) or removed from logo and included in another position on the side of the business card with contact information.
Should not have
• Should not have Harlow Pemberton logo incorporated into Bright Oak Homes logo on both sides of business card. Would like the Bright Oak Homes logo that has Harlow Logo only on the back side of card without contact information.

```html
<!DOCTYPE html>
<html lang="en">
<head>
<meta charset="utf-8">
<title>Merle Dunaway – Business Card</title>
<link rel="stylesheet" href="https://fonts.googleapis.com/css2?family=Play:wght@400;700&family=Cinzel:wght@400;500&family=Tinos&display=swap">
<style>
  :root {
    --canvas: #c9c9cc;
    --card-white: #ffffff;
    --card-black: #1f1f21;
    --bronze-dark: #5a4220;
    --bronze-light: #7b6232;
    --gold-text: #d6b43e;
    --gold-line: #c9a92c;
    --ink-brown: #4b3a1e;
    --light-text: #f4f1ea;
    --watermark: #f0f0f0;
  }
  * { box-sizing: border-box; margin: 0; padding: 0; }
  html, body { width: 1200px; height: 1200px; overflow: hidden; }
  body {
    background: var(--canvas);
    display: flex;
    align-items: center;
    justify-content: center;
    gap: 80px;
  }
  .card {
    width: 400px;
    height: 700px;
    position: relative;
    box-shadow: 0 10px 30px rgba(0,0,0,0.18);
  }

  /* Front: contact side */
  .card-front {
    background: var(--card-white);
    padding: 24px;
    display: flex;
    flex-direction: column;
  }
  .title-band {
    background: linear-gradient(135deg, var(--bronze-light), var(--bronze-dark));
    height: 120px;
    display: flex;
    flex-direction: column;
    align-items: center;
    justify-content: center;
    font-family: "Play", sans-serif;
    color: var(--gold-text);
  }
  .title-band .agent-name { font-size: 30px; font-weight: 700; letter-spacing: 0.5px; }
  .title-band .agent-role { font-size: 21px; margin-top: 2px; }

  .brand-block {
    flex: 1;
    position: relative;
    display: flex;
    flex-direction: column;
    align-items: center;
    justify-content: flex-end;
    padding-bottom: 26px;
  }
  .brand-watermark {
    position: absolute;
    top: 40px;
    left: 50%;
    transform: translateX(-50%);
    width: 200px;
    height: 200px;
    border-radius: 50%;
    background: var(--watermark);
  }
  .brand-name {
    position: relative;
    font-family: "Cinzel", serif;
    font-size: 30px;
    letter-spacing: 3px;
    color: var(--ink-brown);
    text-align: center;
  }
  .brand-tagline {
    position: relative;
    font-family: "Cinzel", serif;
    font-size: 11px;
    letter-spacing: 5px;
    color: var(--ink-brown);
    margin-top: 4px;
  }

  .contact-band {
    background: linear-gradient(135deg, var(--bronze-light), var(--bronze-dark));
    height: 240px;
    display: flex;
    flex-direction: column;
    align-items: center;
    justify-content: center;
    font-family: "Play", sans-serif;
    text-align: center;
  }
  .contact-label { color: var(--light-text); font-size: 15px; margin-top: 8px; }
  .contact-label:first-child { margin-top: 0; }
  .contact-value { color: var(--gold-text); font-size: 17px; }

  /* Back: logo side */
  .card-back {
    background: var(--card-black);
    display: flex;
    align-items: center;
    justify-content: center;
  }
  .card-back .frame {
    position: absolute;
    inset: 18px;
    border: 2px solid var(--gold-line);
  }
  .lockup {
    display: flex;
    align-items: center;
    gap: 12px;
    color: var(--light-text);
    font-family: "Tinos", serif;
  }
  .lockup-mark {
    width: 46px;
    height: 46px;
    border-radius: 50%;
    background: var(--light-text);
    flex-shrink: 0;
  }
  .lockup-text { display: flex; flex-direction: column; align-items: center; }
  .lockup-name { font-size: 25px; line-height: 1; }
  .lockup-agent { font-size: 11px; letter-spacing: 2px; margin-top: 4px; }
  .lockup-tagline { font-size: 6px; letter-spacing: 2px; margin-top: 1px; }
  .partner-badge {
    width: 34px;
    height: 18px;
    background: var(--light-text);
    align-self: flex-start;
    margin-top: 6px;
  }
</style>
</head>
<body>
  <section class="card card-front">
    <header class="title-band">
      <div class="agent-name">MERLE DUNAWAY</div>
      <div class="agent-role">Associate Broker</div>
    </header>
    <div class="brand-block">
      <div class="brand-watermark" role="img" aria-label="Faint brand mark decoration"></div>
      <div class="brand-name">MERLE DUNAWAY</div>
      <div class="brand-tagline">ROOTED IN CARE</div>
    </div>
    <footer class="contact-band">
      <div class="contact-label">cell</div>
      <div class="contact-value">555-307-1948</div>
      <div class="contact-label">web</div>
      <div class="contact-value">www.brightoakhomes.example</div>
      <div class="contact-label">email</div>
      <div class="contact-value">merledunaway@brightoakhomes.example</div>
    </footer>
  </section>

  <section class="card card-back">
    <div class="frame"></div>
    <div class="lockup">
      <div class="lockup-mark"></div>
      <div class="lockup-text">
        <div class="lockup-name">Bright Oak Homes</div>
        <div class="lockup-agent">MERLE DUNAWAY</div>
        <div class="lockup-tagline">ROOTED IN CARE</div>
      </div>
      <div class="partner-badge" role="img" aria-label="Partner brokerage badge"></div>
    </div>
  </section>
</body>
</html>
```